Professional
Miriam T. Hollisby, Esq.
Attorney at Law
Hollisby & Dunmore, LLC
4127 Fernhaven Court
Atlanta, Georgia 30305
mhollisby@hd-counsel.net
www.hd-counsel.net
I may want to include a photo. I have uploaded a photo. I'd like to see if it looks appropriate, if not, we'll go without a photo. Please use the logo that is uploaded
Please use the logo that is uploaded in some way. Possibly the corresponding black background with whitel letters for the back.
Photo to possibly be included on busines cards

```html
<!DOCTYPE html>
<html lang="en">
<head>
<meta charset="utf-8">
<title>Hollisby &amp; Dunmore, LLC — Stationery</title>
<link href="https://fonts.googleapis.com/css2?family=Cormorant+SC:wght@500;600&family=Lato:wght@400&display=swap" rel="stylesheet">
<style>
:root{
  --board:#262626;
  --board-light:#3a3a3a;
  --paper:#ffffff;
  --ink:#3b3b3b;
  --red:#a8151f;
  --red-dark:#5c0a10;
  --black:#141414;
  --blush:#f1d9db;
  --muted:#9a9a9a;
}
*{margin:0;padding:0;box-sizing:border-box}
html,body{width:1200px;height:314px;overflow:hidden}
body{background:radial-gradient(ellipse at 30% 40%,var(--board-light),var(--board) 70%);position:relative;font-family:"Lato",sans-serif;color:var(--ink)}
.serif{font-family:"Cormorant SC",serif;font-weight:600;white-space:nowrap}
.abs{position:absolute}

/* brand block */
.brand{left:24px;top:48px;width:290px;color:var(--paper)}
.brand-mark{font-family:"Cormorant SC",serif;font-weight:600;font-size:16px;letter-spacing:.5px;display:flex;align-items:center;gap:8px;white-space:nowrap}
.brand-mark .dot{flex:none;width:22px;height:22px;border-radius:50%;border:1px solid var(--paper)}
.brand-sub{font-size:6px;letter-spacing:1px;color:var(--muted);margin-top:6px;margin-left:30px}

/* cards */
.card{width:138px;height:44px;box-shadow:0 2px 4px rgba(0,0,0,.5);overflow:hidden}
.card.white{background:var(--paper)}
.card.red{background:linear-gradient(135deg,var(--red),var(--red-dark))}
.card.black{background:var(--black)}
.card .band{position:absolute;left:0;right:0;bottom:0;height:9px;background:linear-gradient(90deg,var(--red-dark),var(--red),var(--red-dark))}
.card .name{position:absolute;left:8px;top:8px;font-size:7px}
.card .line{position:absolute;left:8px;font-size:4px;color:var(--muted);white-space:nowrap}
.card.red .name,.card.black .name{color:var(--paper)}
.card.red .line{color:var(--blush)}

/* letterheads */
.sheet{width:142px;height:282px;background:var(--paper);box-shadow:0 2px 6px rgba(0,0,0,.6)}
.sheet .head{position:absolute;left:8px;top:8px;font-size:6px;color:var(--red)}
.sheet .head-info{position:absolute;right:8px;top:9px;font-size:3.5px;color:var(--muted);text-align:right;line-height:1.4}
.sheet .rule{position:absolute;left:8px;right:8px;top:22px;height:1px;background:var(--blush)}
.faint{position:absolute;font-family:"Cormorant SC",serif;font-weight:600;color:var(--blush);text-align:center;width:100%;white-space:nowrap}
.sheet .faint{top:128px;font-size:13px}
.sheet .foot{position:absolute;left:0;right:0;bottom:0;height:12px;background:linear-gradient(90deg,var(--red-dark),var(--red),var(--red-dark))}
.sheet .foot span{display:block;text-align:center;font-size:3.5px;color:var(--paper);line-height:12px}

/* envelopes */
.env{background:var(--paper);box-shadow:0 2px 6px rgba(0,0,0,.6)}
.env .head{position:absolute;left:8px;top:8px;font-size:6px;color:var(--red)}
.env .addr{position:absolute;left:8px;top:17px;font-size:3.5px;color:var(--muted);line-height:1.4}
.env .faint{top:45%;font-size:14px}
.env .foot{position:absolute;left:0;right:0;bottom:0;height:8px;background:linear-gradient(90deg,var(--red-dark),var(--red),var(--red-dark))}
.flap-set{left:960px;top:18px}
</style>
</head>
<body>

<section class="abs brand">
  <div class="brand-mark"><span class="dot"></span>Hollisby &amp; Dunmore, LLC</div>
  <div class="brand-sub">ATTORNEYS AT LAW</div>
</section>

<!-- business cards -->
<div class="abs card white" style="left:34px;top:190px">
  <div class="name serif" style="color:var(--red)">Hollisby &amp; Dunmore</div>
  <div class="line" style="top:19px">Attorneys at Law</div>
  <div class="band"></div>
</div>
<div class="abs card red" style="left:180px;top:190px">
  <div class="name serif">Miriam T. Hollisby, Esq.</div>
  <div class="line" style="top:19px">Attorney at Law</div>
  <div class="line" style="top:26px">mhollisby@hd-counsel.net</div>
</div>
<div class="abs card white" style="left:34px;top:242px">
  <div class="name serif" style="color:var(--red)">Miriam T. Hollisby, Esq.</div>
  <div class="line" style="top:19px">4127 Fernhaven Court, Atlanta</div>
  <div class="band"></div>
</div>
<div class="abs card black" style="left:180px;top:242px">
  <div class="faint" style="top:14px;font-size:11px;color:var(--paper)">Hollisby &amp; Dunmore</div>
</div>

<!-- letterheads -->
<div class="abs sheet" style="left:336px;top:16px">
  <div class="head serif">Hollisby &amp; Dunmore, LLC</div>
  <div class="head-info">4127 Fernhaven Court<br>Atlanta, Georgia 30305</div>
  <div class="rule"></div>
  <div class="faint">Hollisby &amp; Dunmore</div>
  <div class="foot"><span>www.hd-counsel.net</span></div>
</div>
<div class="abs sheet" style="left:494px;top:16px">
  <div class="head serif">Hollisby &amp; Dunmore, LLC</div>
  <div class="head-info">mhollisby@hd-counsel.net<br>www.hd-counsel.net</div>
  <div class="rule"></div>
  <div class="faint">Hollisby &amp; Dunmore</div>
  <div class="foot"><span>4127 Fernhaven Court · Atlanta, Georgia 30305</span></div>
</div>

<!-- flat envelopes -->
<div class="abs env" style="left:696px;top:92px;width:240px;height:78px">
  <div class="head serif">Hollisby &amp; Dunmore, LLC</div>
  <div class="addr">4127 Fernhaven Court<br>Atlanta, Georgia 30305</div>
  <div class="foot"></div>
</div>
<div class="abs env" style="left:696px;top:186px;width:240px;height:98px">
  <div class="head serif">Hollisby &amp; Dunmore, LLC</div>
  <div class="addr">4127 Fernhaven Court<br>Atlanta, Georgia 30305</div>
  <div class="faint">Hollisby &amp; Dunmore</div>
  <div class="foot"></div>
</div>

<!-- envelope backs with flaps -->
<svg class="abs flap-set" width="220" height="280" viewBox="0 0 220 280">
  <defs>
    <linearGradient id="red-band" x1="0" x2="1">
      <stop offset="0" stop-color="#5c0a10"/><stop offset=".5" stop-color="#a8151f"/><stop offset="1" stop-color="#5c0a10"/>
    </linearGradient>
  </defs>
  <g>
    <rect x="0" y="0" width="216" height="76" fill="#ffffff"/>
    <path d="M0 0 L108 46 L216 0 Z" fill="#141414"/>
    <text x="108" y="26" text-anchor="middle" font-family="Cormorant SC, serif" font-weight="600" font-size="10" fill="#ffffff">Hollisby &amp; Dunmore</text>
  </g>
  <g transform="translate(0,92)">
    <rect x="0" y="0" width="216" height="80" fill="#ffffff"/>
    <path d="M0 0 L108 42 L216 0" fill="#f4f4f4" stroke="#dddddd" stroke-width="1"/>
    <path d="M0 0 L108 42 L216 0 L216 8 L108 50 L0 8 Z" fill="url(#red-band)"/>
    <text x="108" y="70" text-anchor="middle" font-family="Cormorant SC, serif" font-weight="600" font-size="9" fill="#a8151f">Hollisby &amp; Dunmore</text>
  </g>
  <g transform="translate(0,188)">
    <rect x="0" y="0" width="216" height="84" fill="#ffffff"/>
    <path d="M0 0 L108 44 L216 0" fill="#f7f7f7" stroke="#dddddd" stroke-width="1"/>
    <path d="M0 84 L108 48 L216 84" fill="none" stroke="#e6e6e6" stroke-width="1"/>
  </g>
</svg>

</body>
</html>
```